I am looking for a designer for my Gratitude Journal cover design. This is a daily gratitude journal designed for women. The interior features colored pages with a daily gratitude section, weekly habit tracker, and monthly reflection. The journal has enough space for a 12-week journaling.
Book size: 6x 9 inches
Paperback Print Book
Page count: 117
Platform: Pemberly Press
Book title: Bloom Anyway, Dear
Design Style:
-Boho style color and graphics, color choice is free but must follow color psychology, no pure black. The color and styling should correlate to the interior pages (In the attachment).
-There could be a female silhouette on the front cover, but not as big as the whole cover. (doesn’t have to if not looking good)
-No text or interior page preview on the back cover. Only pen name logo on the bottom middle of the back cover and make it small and subtle. (Pen name logo attached)
-Book title on front cover and spine, author name only on spine (Author name: Tobin Vasque).
-No other text on the front cover.
All design elements including fonts must be commercially licensed, and you must provide source files and commercial licenses of them together as part of the delivery.
Target Market(s)
pemberlypress.example

```html
<!DOCTYPE html>
<html lang="en">
<head>
<meta charset="utf-8">
<title>Bloom Anyway, Dear — Cover</title>
<link rel="stylesheet" href="https://fonts.googleapis.com/css2?family=Fraunces:opsz,wght@9..144,600&display=swap">
<style>
  :root {
    --cover-cream: #ebe6da;
    --cover-cream-edge: #e3ddcf;
    --sage-teal: #4f8f86;
    --sage-teal-deep: #457f77;
    --apricot: #eea95a;
    --apricot-sun: #eec48f;
    --ink-navy: #243247;
    --highlight: #f6f3ec;
  }
  * { margin: 0; padding: 0; box-sizing: border-box; }
  html, body {
    width: 980px;
    height: 1200px;
    overflow: hidden;
    background: var(--cover-cream);
  }
  .cover {
    position: relative;
    width: 980px;
    height: 1200px;
    background:
      radial-gradient(ellipse at 50% 40%, rgba(255,255,255,0.25), transparent 70%),
      var(--cover-cream);
    font-family: "Fraunces", Georgia, serif;
  }
  .cover__spine-edge {
    position: absolute;
    left: 0; top: 0; bottom: 0;
    width: 40px;
    background: linear-gradient(90deg, var(--cover-cream-edge), var(--cover-cream));
  }
  .cover__sun {
    position: absolute;
    left: 292px;
    top: 312px;
    width: 440px;
    height: 440px;
    border-radius: 50%;
    background: var(--apricot-sun);
    box-shadow: 6px 4px 0 var(--highlight);
  }
  .cover__figure {
    position: absolute;
    left: 216px;
    top: 196px;
    width: 420px;
    height: 530px;
    border-radius: 48% 52% 30% 22% / 40% 44% 14% 14%;
    background: linear-gradient(160deg, var(--sage-teal) 0%, var(--sage-teal-deep) 100%);
    opacity: 0.95;
  }
  .cover__title {
    position: absolute;
    left: 0; right: 0;
    top: 770px;
    text-align: center;
    font-weight: 600;
    line-height: 1;
    letter-spacing: -0.5px;
  }
  .cover__title-line {
    display: block;
    text-shadow: 4px 3px 0 var(--highlight);
  }
  .cover__title-line--lead {
    color: var(--sage-teal);
    font-size: 76px;
  }
  .cover__title-line--close {
    color: var(--apricot);
    font-size: 112px;
    margin-top: 2px;
  }
  .cover__imprint-mark {
    position: absolute;
    left: 446px;
    top: 1066px;
    width: 84px;
    height: 84px;
    border-radius: 50%;
    background: var(--ink-navy);
  }
</style>
</head>
<body>
  <main class="cover">
    <div class="cover__spine-edge"></div>
    <div class="cover__sun"></div>
    <div class="cover__figure" role="img" aria-label="Boho illustration: sage teal side-profile silhouette of a woman with a hair bun, crescent earring and necklace"></div>
    <h1 class="cover__title">
      <span class="cover__title-line cover__title-line--lead">Bloom Anyway,</span>
      <span class="cover__title-line cover__title-line--close">Dear</span>
    </h1>
    <div class="cover__imprint-mark" role="img" aria-label="Pen name mark"></div>
  </main>
</body>
</html>
```